BARRIER BANNER OTP

I am looking for a visual for a banner
3 meters long by 1 high.
In the same theme as the visual identity of the company.
As simple as possible without overloading

There must be the LOGO, the title TECHNIQUE SERVICES ROUSSEL

_________________________

I am looking for a visual for a banner (barrier banner)
3 meters long by 1 high.

AIR CONDITIONING HEATING VENTILATION
04 52 31 64 19

Font styles to use
Sans Serif

Colors
33b8a4
00a990
33a6d7
0493ce
3176b5
0355a3
ffffff

Requirements
Should not have
• No photo
No photo

```html
<!DOCTYPE html>
<html lang="fr">
<head>
<meta charset="utf-8">
<title>OTP – Banderoles</title>
<link rel="stylesheet" href="https://fonts.googleapis.com/css2?family=Arimo:wght@700&display=swap">
<style>
  :root {
    --page: #e5e6e8;
    --panel: #fdfdfd;
    --ink: #2f3c47;
    --muted: #7a909c;
    --accent: #2b93c4;
  }
  html, body {
    margin: 0;
    width: 1173px;
    height: 1200px;
    overflow: hidden;
    background: var(--page);
    font-family: "Arimo", Arial, sans-serif;
    font-weight: 700;
  }
  .banner {
    position: absolute;
    background: var(--panel);
    box-shadow: 0 4px 12px rgba(0,0,0,0.28);
  }
  .banner--side { left: 77px; top: 52px; width: 1032px; height: 344px; }
  .banner--contact { left: 74px; top: 424px; width: 1032px; height: 345px; }
  .banner--large { left: 85px; top: 805px; width: 1030px; height: 343px; }

  .brand {
    position: absolute;
    display: flex;
    align-items: flex-end;
    gap: 14px;
    color: var(--ink);
    line-height: 0.8;
    letter-spacing: 2px;
  }
  .brand__square {
    width: 0.28em;
    height: 0.28em;
    background: var(--accent);
    align-self: flex-start;
    order: 2;
  }
  .banner--side .brand { left: 25px; top: 125px; font-size: 150px; }
  .banner--contact .brand { left: 0; right: 0; justify-content: center; top: 18px; font-size: 170px; }
  .banner--large .brand { left: 27px; top: 95px; font-size: 222px; }

  .title {
    position: absolute;
    white-space: nowrap;
    margin: 0;
    letter-spacing: 0.2px;
  }
  .banner--side .title { left: 336px; top: 204px; font-size: 38px; color: var(--muted); }
  .banner--large .title { left: 469px; top: 252px; font-size: 31px; color: var(--muted); }
  .banner--contact .title { left: 0; right: 0; text-align: center; top: 170px; font-size: 39px; color: var(--ink); }

  .website {
    position: absolute;
    left: 0; right: 0; top: 228px;
    text-align: center;
    font-size: 27px;
    color: var(--ink);
  }
  .phone {
    position: absolute;
    left: 0; right: 0; top: 272px;
    text-align: center;
    font-size: 48px;
    color: var(--ink);
    letter-spacing: 1px;
  }
</style>
</head>
<body>
  <section class="banner banner--side">
    <div class="brand"><span class="brand__name">OTP</span><span class="brand__square"></span></div>
    <p class="title">TECHNIQUE SERVICES ROUSSEL</p>
  </section>

  <section class="banner banner--contact">
    <div class="brand"><span class="brand__name">OTP</span><span class="brand__square"></span></div>
    <p class="title">TECHNIQUE SERVICES ROUSSEL</p>
    <p class="website" style="margin:0">technique-services-roussel.fr</p>
    <p class="phone" style="margin:0">04 52 31 64 19</p>
  </section>

  <section class="banner banner--large">
    <div class="brand"><span class="brand__name">OTP</span><span class="brand__square"></span></div>
    <p class="title">TECHNIQUE SERVICES ROUSSEL</p>
  </section>
</body>
</html>
```